Charting the Northern Ridge *

Bold eye-catching design for business non-fiction: I am seeking a bold, and clean design for a book. The book will be 6X9 for both the ebook and in print. I am open to ideas, but found that books like “tall and brave” with contrast are highly desirable for business books.

I am open to color choices.

I would also like a growth orientated graphic in the book - something to show growth, leadership, movement. Not just a plain graphic.

The title:

Charting the Northern Ridge

The subtitle - I am open to suggestions. Two subtitles I am considering:

A framework for new sales leaders and those who want to keep winning.

A guide for new sales leaders and those who want to keep winning.

The below is an introduction of the book: (Back Jacket)

Sales transformation is a topic that is infrequently written about. For the new sales leader, there are a myriad of books written on coaching, leadership, forecasting, solution selling and sales process but very little is written about how to assess a sales team and build a plan for long-term success.

Through my sales leadership career, whether recently promoted or starting with a new team, I have often asked the question: Where do I start?

In the end, I was disappointed with the answers from currently available books and research, left to figure it out myself - which I did over a decade, with great pain and through many transformations. The inability to answer the question – Where do I start? – is why I wrote this book. To answer that question.

The goal of this book is to help sales leaders answer that question by providing a framework to understand the business, build a plan, and guide the team through the different stages of a sales transformation. A framework to succeed at the fastest pace possible, quarter after quarter.

(End back jacket - the rest is just additional context)

Over the last decade, I have had the privilege of leading teams in North America, Europe, and Asia. I have led turnarounds, growth businesses, and realignments. Each team was different in size, complexity, and culture; and each one offered up new and unique challenges. Each team operated with different market dynamics: one was a commodity; one was a low-cost leader; one was a market innovator. Each transformation helped me learn by taking risks, by failing and by succeeding. At each step, I had many teachers; and as I learned, I made notes. Over time I built a framework that you can leverage as you read and absorb this book. As you lead your team through a sales transformation.

I hope that this book will become for you what One Hundred Mornings is for me: a favorite on your bookshelf; underlined, highlighted, dog-eared, and an ongoing reference.

Sales leadership is a journey. It is never linear, and it is always changing. At different times, different parts of this book will apply, while others will not, but hopefully, you will find it a useful and long-lasting reference.
Updates

Target Market(s)

Business readers. Sales leaders.

Requirements
Must have
• Modern, clear, eye catching colours. Clean. Graphics that indicate growth, leadership, strength.
• Please ensure the design has the full cover and back jacket design. Please use the introduction of the book as the back jacket text.

```html
<!DOCTYPE html>
<html lang="en">
<head>
<meta charset="utf-8">
<title>Charting the Northern Ridge – Cover Spread</title>
<link rel="stylesheet" href="https://fonts.googleapis.com/css2?family=Tinos:ital,wght@0,400;0,700;1,400&display=swap">
<style>
  :root {
    --stage: #000000;
    --paper: #ffffff;
    --ink: #1f1f1f;
    --accent: #c1272d;
    --accent-soft: rgba(193, 39, 45, 0.9);
    --accent-faint: rgba(193, 39, 45, 0.28);
    --maze-light: #f2f2f2;
    --maze-shade: #d4d4d4;
  }
  * { margin: 0; padding: 0; box-sizing: border-box; }
  html, body { width: 1200px; height: 1200px; overflow: hidden; background: var(--stage); }
  .canvas { position: relative; width: 1200px; height: 1200px; background: var(--stage); font-family: "Tinos", "Times New Roman", serif; color: var(--ink); }

  .jacket { position: absolute; left: 42px; top: 243px; width: 1120px; height: 795px; background: var(--paper); overflow: hidden; }

  .back-art { position: absolute; left: 0; top: 0; width: 590px; height: 330px;
    background:
      linear-gradient(180deg, rgba(255,255,255,0) 45%, var(--paper) 100%),
      linear-gradient(-55deg, rgba(193,39,45,0) 38%, var(--accent-faint) 44%, var(--accent-faint) 50%, rgba(193,39,45,0) 56%),
      repeating-linear-gradient(90deg, var(--maze-light) 0 46px, var(--maze-shade) 46px 58px),
      linear-gradient(180deg, var(--maze-shade) 0%, var(--maze-light) 100%); }

  .front-art { position: absolute; left: 590px; top: 0; width: 530px; height: 380px;
    background:
      linear-gradient(180deg, rgba(255,255,255,0) 55%, var(--paper) 92%),
      linear-gradient(62deg, rgba(193,39,45,0) 44%, var(--accent-soft) 47%, var(--accent-soft) 53%, rgba(193,39,45,0) 56%),
      repeating-linear-gradient(90deg, var(--maze-light) 0 52px, var(--maze-shade) 52px 66px),
      linear-gradient(180deg, var(--maze-shade) 0%, var(--maze-light) 100%); }

  .blurb { position: absolute; left: 80px; top: 180px; width: 371px; font-size: 14.8px; line-height: 19.6px; text-align: justify; }
  .blurb p { margin-bottom: 19.6px; }
  .blurb strong { font-weight: 700; }

  .barcode-space { position: absolute; left: 331px; top: 666px; width: 157px; height: 93px; background: var(--accent); }

  .spine { position: absolute; left: 566px; top: 60px; width: 0; height: 0; }
  .spine-title, .spine-author { position: absolute; white-space: nowrap; transform-origin: 0 0; transform: rotate(90deg) translateY(-100%); }
  .spine-title { top: 0; left: -18px; font-size: 36px; }
  .spine-author { top: 485px; left: -12px; font-size: 21px; font-weight: 700; }
  .accent { color: var(--accent); }

  .front-title { position: absolute; left: 590px; top: 0; width: 455px; height: 640px; font-weight: 400; line-height: 1; }
  .front-title span { position: absolute; right: 0; white-space: nowrap; }
  .title-line-1 { top: 333px; font-size: 115px; letter-spacing: -1px; }
  .title-line-2 { top: 461px; }
  .title-the { position: static !important; font-size: 58px; }
  .title-northern { position: static !important; font-size: 100px; color: var(--accent); letter-spacing: -1px; }
  .title-line-3 { top: 549px; font-size: 72px; }

  .subtitle { position: absolute; left: 650px; top: 628px; width: 490px; text-align: center; font-style: italic; font-size: 20px; line-height: 31px; letter-spacing: -0.5px; }
  .author { position: absolute; left: 650px; top: 718px; width: 490px; text-align: center; font-weight: 700; font-size: 34px; letter-spacing: 0.5px; }
</style>
</head>
<body>
<div class="canvas">
  <section class="jacket">
    <div class="back-art" role="img" aria-label="Faded white maze with a red path arrow running down through it"></div>
    <div class="front-art" role="img" aria-label="White 3D maze with a bold red arrow cutting through it and pointing down-right"></div>

    <div class="blurb">
      <p><strong>Sales transformation</strong> is a topic that is infrequently written about. For the new sales leader, there are a myriad of books written on coaching, leadership, forecasting, solution selling and sales process but very little is written about how to assess a sales team and build a plan for long-term success.</p>
      <p>Through my sales leadership career, whether recently promoted or starting with a new team, I have often asked the question: Where do I start?</p>
      <p>In the end, I was disappointed with the answers from currently available books and research, left to figure it out myself - which I did over a decade, with great pain and through many transformations. The inability to answer the question – Where do I start? – is why I wrote this book. To answer that question.</p>
      <p>The goal of this book is to help sales leaders answer that question by providing a framework to understand the business, build a plan, and guide the team through the different stages of a sales transformation. A framework to succeed at the fastest pace possible, quarter after quarter.</p>
    </div>
    <div class="barcode-space"></div>

    <div class="spine">
      <div class="spine-title">Charting the <span class="accent">Northern</span> Ridge</div>
      <div class="spine-author">DANIEL HAVERLY</div>
    </div>

    <h1 class="front-title">
      <span class="title-line-1">Charting</span>
      <span class="title-line-2"><span class="title-the">the </span><span class="title-northern">Northern</span></span>
      <span class="title-line-3">Ridge</span>
    </h1>
    <p class="subtitle">A Guide for New Sales Leaders<br>and Those Who Want to Keep Winning</p>
    <p class="author">DANIEL HAVERLY</p>
  </section>
</div>
</body>
</html>
```